K&T Fixit and Rebuild general contracting business card design

I already have a logo that I want to use and I need a card that uses that logo and color scheme on the front with the address phone numbers and email and on the back a place for technicians to write in their name and phone number when they hand it out. It will need the License number of License #KTFXTRB318QN.
It should say General Contractor under the company name. The address is
4417 NE 3rd Ave, Ste D246
Vancouver, WA 98612
www.kandtfixitandrebuild.example
office@kandtfixitandrebuild.example
360-555-0182 is the telephone number
360-555-0149 is the fax number

Target Market(s)

Homeowners needing remodel work or repairs in their home.

Industry/Entity Type

Construction

Contact Information for Business Card

Business name, address, phone number, license number, fax number, email, and website on the front and a place to fill in technician's name and number

Font styles to use
Serif

Requirements
Must have
• Business name, address, phone number, license number, fax number, email, and website on the front and a place to fill in technician's name and number
Nice to have
• I uploaded an example of a front that is good.
Should not have
• Froo froo or extra embellishments.

```html
<!DOCTYPE html>
<html lang="en">
<head>
<meta charset="utf-8">
<title>K&amp;T Fixit and Rebuild – Business Card</title>
<link rel="stylesheet" href="https://fonts.googleapis.com/css2?family=Roboto:wght@400;500;700&display=swap">
<style>
  :root {
    --backdrop: #7a5f40;
    --card-black: #050505;
    --card-band: #1a0906;
    --wood-dark: #4a1a0e;
    --wood-mid: #7a3220;
    --wood-light: #8e4428;
    --copper: #c27a4f;
    --white: #ffffff;
    --paper: #f7f7f7;
    --ink: #111111;
    --ghost: #eadbcb;
  }
  * { margin: 0; padding: 0; box-sizing: border-box; }
  html, body { width: 900px; height: 1200px; overflow: hidden; }
  body {
    position: relative;
    background: var(--backdrop);
    font-family: "Roboto", Arial, sans-serif;
  }
  .card {
    position: absolute;
    width: 773px;
    height: 448px;
    border-radius: 20px;
    overflow: hidden;
  }
  /* Front */
  .card-front { left: 72px; top: 135px; background: var(--card-black); }
  .front-band {
    position: absolute; left: 0; top: 287px; width: 100%; height: 28px;
    background: var(--card-band);
  }
  .front-wood {
    position: absolute; left: 0; top: 315px; width: 100%; height: 133px;
    background: linear-gradient(180deg, var(--wood-mid) 0%, var(--wood-light) 40%, var(--wood-dark) 100%);
  }
  .brand-mark {
    position: absolute; left: 61px; top: 70px; width: 320px;
    display: flex; align-items: flex-start; gap: 16px;
  }
  .brand-square {
    flex: none; width: 22px; height: 22px; margin-top: 14px;
    background: var(--copper);
  }
  .brand-name {
    font-weight: 700; font-size: 46px; line-height: 1.1;
    color: var(--copper);
  }
  .company-info {
    position: absolute; left: 423px; top: 76px;
    color: var(--white); font-size: 20px; line-height: 27px;
  }
  .company-name { font-weight: 700; font-size: 24px; line-height: 30px; }
  .company-role { margin-bottom: 21px; }
  .company-address { margin-bottom: 16px; }
  .contact-web, .contact-phone {
    position: absolute; top: 350px;
    color: var(--white); font-size: 19px; line-height: 35px; font-weight: 500;
  }
  .contact-web { left: 61px; }
  .contact-phone { left: 521px; }

  /* Back */
  .card-back { left: 74px; top: 625px; background: var(--paper); }
  .ghost-name {
    position: absolute; left: 0; top: 80px; width: 100%;
    text-align: center; font-weight: 700; font-size: 92px; line-height: 1.05;
    color: var(--ghost);
  }
  .fill-row {
    position: absolute; left: 77px; right: 70px;
    display: flex; align-items: flex-end; gap: 10px;
    font-size: 19px; letter-spacing: 2px; color: var(--ink);
  }
  .fill-row .fill-line { flex: 1; border-bottom: 2px solid var(--ink); margin-bottom: 4px; }
  .row-name { top: 160px; }
  .row-phone { top: 235px; }
  .back-web {
    position: absolute; left: 0; bottom: 35px; width: 100%;
    text-align: center; font-size: 21px; font-weight: 500; letter-spacing: 2px;
    color: var(--ink);
  }
</style>
</head>
<body>
  <section class="card card-front">
    <div class="brand-mark">
      <span class="brand-square"></span>
      <span class="brand-name">K&amp;T Fixit and Rebuild</span>
    </div>
    <div class="company-info">
      <div class="company-name">K&amp;T Fixit and Rebuild</div>
      <div class="company-role">General Contractor</div>
      <div class="company-address">4417 NE 3rd Ave, Ste D246<br>Vancouver, WA 98612</div>
      <div class="company-license">License #KTFXTRB318QN</div>
    </div>
    <div class="front-band"></div>
    <div class="front-wood" role="img" aria-label="Dark reddish wood grain texture band"></div>
    <div class="contact-web">
      www.kandtfixitandrebuild.example<br>
      office@kandtfixitandrebuild.example
    </div>
    <div class="contact-phone">
      Tel: 360-555-0182<br>
      Fax: 360-555-0149
    </div>
  </section>

  <section class="card card-back">
    <div class="ghost-name" aria-hidden="true">K&amp;T Fixit<br>and Rebuild</div>
    <div class="fill-row row-name"><span>NAME</span><span class="fill-line"></span></div>
    <div class="fill-row row-phone"><span>PHONE NUMBER</span><span class="fill-line"></span></div>
    <div class="back-web">www.kandtfixitandrebuild.example</div>
  </section>
</body>
</html>
```